Business card design

I need my logo on this card, things I need the card to have on it
licensed and insured.
owner operators Derek & Milton Halvorsen
my phone number 5418237906
Disaster Recovery, Storm Damage Restoration, Proactive Disaster Plan Management, Roof Repair/Restoration Structural Repair and Reconstruction, Emergency Boarding and Tarping Service, Perimeter Fencing, Emergency Tree Removal,

```html
<!DOCTYPE html>
<html lang="en">
<head>
<meta charset="utf-8">
<title>Halvorsen's Construction L.L.C – Business Card</title>
<link rel="stylesheet" href="https://fonts.googleapis.com/css2?family=Montserrat:wght@400;500;700;800&display=swap">
<style>
  :root {
    --backdrop: #3a3330;
    --card: #1f2022;
    --card-edge: #141516;
    --blue: #3a8fd6;
    --grey: #6e6f72;
    --grey-dark: #4d4e51;
    --white: #ffffff;
    --soft: #d9dadc;
  }
  * { box-sizing: border-box; margin: 0; padding: 0; }
  html, body {
    width: 1200px; height: 786px; overflow: hidden;
    background: var(--backdrop);
    font-family: "Montserrat", sans-serif;
  }
  .stage {
    position: relative; width: 1200px; height: 786px;
    display: flex; align-items: center; justify-content: center; gap: 40px;
  }
  .card {
    position: relative; width: 540px; height: 310px;
    background: var(--card);
    overflow: hidden;
    box-shadow: 0 10px 30px rgba(0,0,0,.45);
  }

  /* Brand name (used on both sides) */
  .brand { color: var(--blue); font-weight: 500; line-height: 1.05; }
  .brand-mark {
    display: inline-block; width: 14px; height: 14px;
    background: var(--blue); margin-bottom: 10px;
  }
  .brand-name { font-size: 34px; letter-spacing: 1px; }
  .brand-sub { font-size: 11px; letter-spacing: 6px; margin-top: 6px; }

  /* Front */
  .front .brand { position: absolute; left: 36px; top: 58px; }
  .phone-band {
    position: absolute; right: 0; top: 152px;
    width: 250px; height: 48px;
    background: var(--blue);
    display: flex; align-items: center; gap: 12px; padding-left: 22px;
    color: var(--white); font-size: 23px; font-weight: 500; letter-spacing: .5px;
  }
  .phone-band svg { width: 20px; height: 20px; flex: none; }
  .licensed {
    position: absolute; right: 36px; top: 218px;
    display: flex; align-items: center; gap: 14px;
    color: var(--blue); font-size: 13px; font-weight: 500;
  }
  .licensed svg { width: 9px; height: 12px; }
  .grey-block {
    position: absolute; left: 210px; bottom: 56px;
    width: 80px; height: 50px; background: var(--grey-dark);
  }
  .owners { position: absolute; left: 36px; top: 196px; }
  .owners-names { color: var(--blue); font-size: 21px; font-weight: 800; }
  .owners-role { color: var(--white); font-size: 12px; font-weight: 500; margin-top: 3px; }
  .email-band {
    position: absolute; left: 0; bottom: 0;
    width: 290px; height: 56px;
    background: var(--grey);
    display: flex; align-items: center; gap: 14px; padding-left: 36px;
    color: var(--white); font-size: 13px;
  }
  .email-band svg { width: 16px; height: 12px; flex: none; }

  /* Back */
  .back .brand { position: absolute; left: 60px; top: 112px; }
  .back .brand-name { font-size: 30px; }
  .back .brand-sub { font-size: 10px; letter-spacing: 5px; }
  .divider {
    position: absolute; left: 290px; top: 70px;
    width: 1px; height: 150px; background: var(--blue);
  }
  .services { position: absolute; left: 306px; top: 66px; width: 225px; }
  .services-title { color: var(--blue); font-size: 14px; font-weight: 800; margin-bottom: 4px; }
  .services-list { list-style: none; color: var(--soft); font-size: 9.5px; line-height: 1.45; }
  .services-list li { position: relative; padding-left: 9px; }
  .services-list li::before {
    content: ""; position: absolute; left: 0; top: 5px;
    width: 3px; height: 3px; border-radius: 50%; background: var(--blue);
  }
</style>
</head>
<body>
<main class="stage">
  <section class="card front" aria-label="Card front">
    <div class="brand">
      <span class="brand-mark"></span>
      <div class="brand-name">HALVORSEN'S</div>
      <div class="brand-sub">CONSTRUCTION L.L.C</div>
    </div>

    <div class="phone-band">
      <svg viewBox="0 0 20 20" aria-hidden="true">
        <path fill="#fff" d="M2 7c0-2 3-4 8-4s8 2 8 4v1h-4V6.5c-1-.5-2.5-.7-4-.7s-3 .2-4 .7V8H2z"/>
        <rect x="4" y="9" width="12" height="8" rx="1.5" fill="#fff"/>
        <g fill="#3a8fd6"><circle cx="8" cy="12" r=".8"/><circle cx="10" cy="12" r=".8"/><circle cx="12" cy="12" r=".8"/><circle cx="8" cy="14.5" r=".8"/><circle cx="10" cy="14.5" r=".8"/><circle cx="12" cy="14.5" r=".8"/></g>
      </svg>
      <span>5418237906</span>
    </div>

    <div class="licensed">
      <svg viewBox="0 0 9 12" aria-hidden="true"><path fill="#3a8fd6" d="M0 0l9 6-9 6z"/></svg>
      <span>licensed and insured</span>
    </div>

    <div class="grey-block"></div>

    <div class="owners">
      <div class="owners-names">Derek &amp; Milton Halvorsen</div>
      <div class="owners-role">Owner Operators</div>
    </div>

    <div class="email-band">
      <svg viewBox="0 0 16 12" aria-hidden="true">
        <rect x="0.5" y="0.5" width="15" height="11" fill="#fff"/>
        <path d="M1 1l7 6 7-6" fill="none" stroke="#6e6f72" stroke-width="1.3"/>
      </svg>
      <span>info@halvorsenbuild.com</span>
    </div>
  </section>

  <section class="card back" aria-label="Card back">
    <div class="brand">
      <span class="brand-mark"></span>
      <div class="brand-name">HALVORSEN'S</div>
      <div class="brand-sub">CONSTRUCTION L.L.C</div>
    </div>
    <div class="divider"></div>
    <div class="services">
      <h2 class="services-title">Our Services</h2>
      <ul class="services-list">
        <li>Disaster Recovery,</li>
        <li>Storm Damage Restoration</li>
        <li>Proactive Disaster Plan Management,</li>
        <li>Roof Repair/Restoration Structural Repair and Reconstruction</li>
        <li>Emergency Boarding and Tarping Service</li>
        <li>Perimeter Fencing,</li>
        <li>Emergency Tree Removal</li>
      </ul>
    </div>
  </section>
</main>
</body>
</html>
```